Landing Page für Freelancer im Bereich der Informationstechnik
Zielgruppe
Ich bin Experte für Informationstechnik, Unified Communications, Beratung, Management sowie Projekte aller Art.
Mit meiner WOLKENTOR GmbH bin ich als (einzelner) Freelancer für mittelständische Unternehmen und Konzerne in verschiedensten Projekten tätig.
Mein Motto lautet 'Mit Präzision und langjähriger Erfahrung immer alles im Griff!'
Aufgabenstellung
Die aktuell existierende Internet-Präsenz unter wolkentor-web.de beinhaltet aktuell nur eine minimalistische statische Seite sowie das Impressum, ohne jegliche dynamische Inhalte.
DABEI SOLL ES BLEIBEN. Auch die Inhalte sollen unverändert übernommen werden.
Lediglich soll jetzt eine Anlehnung an das zwischenzeitlich vorhandene Logo vorgenommen werden, welches ich mitliefere.
Es geht mir insgesamt nur darum, ein professionelleres Auftreten zu haben, WENN sich denn mal jemand auf die Seite verirrt.
Das Aussehen soll daher modern und dynamisch sein.
ZUSAMMENFASSUNG: Inhalte bleiben 1:1, grafische Anpassung an Logo gewünscht.
Technisch: Statisch, kein Content-Management. Lohnt sich hier nicht.
SEHR WICHTIG: Ich möchte gerne, dass die Lieferung bereits als HTML (und NICHT NUR ALS GRAFIK) erfolgt, ggf. stelle ich auch kurz den FTP-Zugang.
Insgesamt möchte ich gar keine große Sache draus machen.
Viele Anpassungsrunden wird es voraussichtlich nicht geben.
Zeitlich ist dies hier ein sehr kleines Projekt - Erweiterungen kommen später.

```html
<!DOCTYPE html>
<html lang="de">
<head>
<meta charset="utf-8">
<title>Lukas Benedikt Harms – WOLKENTOR GmbH</title>
<link rel="stylesheet" href="https://fonts.googleapis.com/css2?family=Outfit:wght@400;500;600&display=swap">
<style>
  :root {
    --teal: #53a6bf;
    --ink: #3a3a3c;
    --paper: #ffffff;
    --desk-light: #d6dce5;
    --desk-dark: #b7c2d0;
  }
  * { margin: 0; padding: 0; box-sizing: border-box; }
  html, body {
    width: 1047px; height: 1200px; overflow: hidden;
    background: var(--paper);
    font-family: "Outfit", sans-serif;
    color: var(--ink);
  }
  .page { position: relative; width: 1047px; height: 1200px; }

  .main-nav { position: absolute; top: 88px; left: 102px; display: flex; gap: 37px; }
  .main-nav a { color: var(--ink); text-decoration: none; font-size: 12.5px; font-weight: 500; }

  .brand {
    position: absolute; top: 130px; left: 773px; width: 172px;
    display: flex; align-items: center; justify-content: center; gap: 8px;
    color: var(--teal); font-size: 17px; font-weight: 500; letter-spacing: 1.5px;
  }
  .brand-dot { width: 10px; height: 10px; border-radius: 50%; background: var(--teal); }

  .degree { position: absolute; top: 205px; left: 102px; font-size: 22px; font-weight: 500; }
  .person-name { position: absolute; top: 248px; left: 100px; font-size: 43px; font-weight: 500; color: var(--teal); letter-spacing: -0.3px; }
  .master { position: absolute; top: 318px; left: 102px; font-size: 21.5px; font-weight: 500; }

  .contact-mail {
    position: absolute; top: 423px; left: 102px;
    font-size: 12px; font-weight: 500; color: var(--ink); text-decoration: none;
    border-bottom: 1px solid var(--teal); padding-bottom: 1px;
  }

  .services {
    position: absolute; top: 420px; left: 431px; width: 530px;
    font-size: 30.5px; font-weight: 500; line-height: 40px; letter-spacing: -0.2px;
  }
  .intro {
    position: absolute; top: 563px; left: 431px; width: 520px;
    font-size: 12px; font-weight: 500; line-height: 18.4px;
  }

  .banner { position: absolute; top: 690px; left: 102px; width: 855px; height: 428px; display: flex; }
  .banner-claim {
    width: 329px; height: 100%; background: var(--teal); color: var(--paper);
    display: flex; flex-direction: column; align-items: center;
  }
  .banner-brand {
    margin-top: 142px; display: flex; align-items: center; gap: 6px;
    font-size: 13px; font-weight: 500; letter-spacing: 1.2px;
  }
  .banner-brand .brand-dot { width: 7px; height: 7px; background: var(--paper); }
  .motto {
    margin-top: 80px; text-align: center; text-transform: uppercase;
    font-size: 18px; font-weight: 600; line-height: 27.7px;
  }
  .banner-visual { flex: 1; height: 100%; background: linear-gradient(135deg, var(--desk-light), var(--desk-dark)); }
</style>
</head>
<body>
<div class="page">
  <nav class="main-nav">
    <a href="#">Startseite</a>
    <a href="#">Impressum</a>
    <a href="#">Datenschutz</a>
  </nav>

  <div class="brand"><span class="brand-dot"></span>WOLKENTOR GmbH</div>

  <p class="degree">Diplom-Informatiker (FH)</p>
  <h1 class="person-name">Lukas Benedikt Harms</h1>
  <p class="master">Master of Science in Electronic Business</p>

  <a class="contact-mail" href="#">l punkt harms at wolkentor-web punkt de</a>

  <h2 class="services">Experte für Informationstechnik | Unified Communications | Beratung | Management | Projekte aller Art</h2>
  <p class="intro">Gerne schicke ich Ihnen unverbindlich mein Expertenprofil samt CV sowie meine aktuellen Verfügbarkeiten zu. Kontaktieren Sie mich hierzu einfach per E-Mail unter l punkt harms at wolkentor-web punkt de. Ich freue mich auf Sie!</p>

  <section class="banner">
    <div class="banner-claim">
      <div class="banner-brand"><span class="brand-dot"></span>WOLKENTOR GmbH</div>
      <p class="motto">"Mit Präzision<br>und langjähriger<br>Erfahrung immer<br>alles im Griff!"</p>
    </div>
    <div class="banner-visual" role="img" aria-label="Illustration eines Schreibtischs von oben mit Laptops, Tablet, Notizen, Taschenrechner und Diagrammen"></div>
  </section>
</div>
</body>
</html>
```